looking for sleek business card to standout from the crowd!

We are a young biotechnology company looking to help you personalize your health through understanding your genetic make up. We need you help in making a clean but sleek business card design using our new logo. The goal? Any time we give our cards out, people say "nice card!" The feel we are going for is "modern-techy". We don't want to come across as an old, giant pharma company, but not trying to be a hipster either.

Target Market(s)

healthcare and biotechnology industry.

Industry/Entity Type

Biotechnology

Contact Information for Business Card

Info to include on the card will be NAME, TITLE, EMAIL, PHONE. The companies website (www.corvalinbio.com) should also be on the card some where. Would like the logo, when printed, to be raised.

Requirements
Must have
• The logo we have attached in the color it is in. Fonts for text should lean toward more professional/tech.
Nice to have
• Prefer white/light color background
Should not have
• cartoons, landscape backgrounds images.

```html
<!DOCTYPE html>
<html lang="en">
<head>
<meta charset="utf-8">
<title>Corvalin Business Card</title>
<link href="https://fonts.googleapis.com/css2?family=Comfortaa:wght@300;400;700&display=swap" rel="stylesheet">
<style>
  :root{
    --stage:#2aa8f0;
    --card:#ffffff;
    --brand-blue:#1d72bd;
    --ink:#1f2a36;
    --band-text:#ffffff;
  }
  *{box-sizing:border-box;margin:0;padding:0}
  html,body{width:1200px;height:803px;overflow:hidden}
  body{background:var(--stage);font-family:"Comfortaa",sans-serif;position:relative}
  .card{
    position:absolute;left:250px;top:201px;width:700px;height:400px;
    background:var(--card);box-shadow:0 10px 30px rgba(0,40,90,.35);overflow:hidden;
  }
  .brand{position:absolute;left:48px;top:40px}
  .brand-name{font-weight:700;font-size:44px;letter-spacing:2px;color:var(--brand-blue);line-height:1}
  .tagline-band{
    position:absolute;left:0;top:122px;width:100%;height:46px;background:var(--brand-blue);
    display:flex;align-items:center;justify-content:flex-end;padding-right:150px;
  }
  .tagline{color:var(--band-text);font-weight:300;font-size:19px;letter-spacing:1px;text-transform:uppercase}
  .contacts{position:absolute;top:205px;display:flex;flex-direction:column;gap:16px}
  .contacts--phone{left:40px}
  .contacts--web{left:330px;top:225px}
  .contact{display:flex;align-items:center;gap:10px;font-size:15px;font-weight:400;color:var(--ink)}
  .contact svg{width:22px;height:22px;flex:none}
  .address-band{
    position:absolute;left:0;top:322px;width:100%;height:44px;background:var(--brand-blue);
    display:flex;align-items:center;gap:10px;padding-left:30px;
    color:var(--band-text);font-size:15px;font-weight:300;white-space:nowrap;
  }
  .address-band svg{width:22px;height:22px;flex:none}
</style>
</head>
<body>
  <div class="card">
    <div class="brand">
      <span class="brand-name">CORVALIN</span>
    </div>

    <div class="tagline-band"><span class="tagline">Personalize your health</span></div>

    <div class="contacts contacts--phone">
      <div class="contact">
        <svg viewBox="0 0 24 24" fill="none" stroke="currentColor" stroke-width="1.5"><circle cx="12" cy="12" r="10.5"/><path d="M7 10c0-2 10-2 10 0v1h-3v-1H10v1H7z" fill="currentColor"/><path d="M8 12h8l1 4H7z" fill="currentColor"/></svg>
        <span>Tel: 00 478210395</span>
      </div>
      <div class="contact">
        <svg viewBox="0 0 24 24" fill="none" stroke="currentColor" stroke-width="1.5"><circle cx="12" cy="12" r="10.5"/><rect x="7" y="11" width="10" height="6" fill="currentColor"/><rect x="9" y="7" width="6" height="4"/></svg>
        <span>Fax: 00 478210395</span>
      </div>
    </div>

    <div class="contacts contacts--web">
      <div class="contact">
        <svg viewBox="0 0 24 24" fill="none" stroke="currentColor" stroke-width="1.5"><circle cx="12" cy="12" r="10.5"/><rect x="6.5" y="8" width="11" height="8"/><path d="M6.5 8l5.5 4.5L17.5 8"/></svg>
        <span>info@corvalinbio.com</span>
      </div>
      <div class="contact">
        <svg viewBox="0 0 24 24" fill="none" stroke="currentColor" stroke-width="1.5"><circle cx="12" cy="12" r="10.5"/><rect x="6.5" y="7.5" width="11" height="7.5"/><path d="M10 18h4M12 15v3"/></svg>
        <span>http://corvalinbio.com</span>
      </div>
    </div>

    <div class="address-band">
      <svg viewBox="0 0 24 24" fill="none" stroke="currentColor" stroke-width="1.5"><circle cx="12" cy="12" r="10.5"/><path d="M12 18s-4-4.5-4-7.5a4 4 0 0 1 8 0C16 13.5 12 18 12 18z"/><circle cx="12" cy="10.5" r="1.4" fill="currentColor"/></svg>
      <span>P.O Box: 5820, Harrow Lane, Office No: 310, Leeds, United Kingdom</span>
    </div>
  </div>
</body>
</html>
```